Business Card Design Project for Harbourlight Homes

We need a business card design for Harbourlight Homes Ltd, a respected building company that specialises in high quality designer homes.

We're after a sleek, clean, modern business card (could even have an interesting shape or something different from normal business cards) with wow factor that people will remember. It also needs to look sharp and great on print.

Please see example attached (do not copy, for inspiration only).

It needs to be in line with the new logo (see attached) and look consistent with that.

The new business card should include the Trusted Trades logo (see attached) as well as the company logo and the two need to look balanced and sleek in regards to their position on the card.
_______________________________________________________
Details to be included:
Tobin Vareck
Director

M: 021 555 0148
E: milo@harbourlighthomes.example
W: www.harbourlighthomes.example

If you present an option for an open card, here's some additional wording we would like you to use:

Harbourlight Homes are a highly skilled team who specialises in residential projects, from simple homes through to top end architectural designs.
We will treat your project with integrity, the attention it deserves, and we guarantee 100% satisfaction.

Timeless craftsmanship. Uncompromising standards.

___________________________________________________________
Additional info on Harbourlight Homes for your consideration:

The core values of the company are integrity, trust, expertise and uncompromising standards.

Harbourlight Homes have been building homes for over 20 years. Only residential, from simple 2-3 bedroom homes through to top end architectural designs. They are a registered Trusted Trade (the Trusted Trades Federation is a highly trusted and respected organisation in New Zealand).

The team at Harbourlight Homes pride themselves in delivering impeccable service to their clients and position themselves as their trusted partners and friends in the construction of their most valuable asset.

Thanks! We look forward to your designs!!!

Target Market(s)

People 30 yrs+ who have an interest in owning quality homes and are prepared to pay for it. Homes built to standards, future-proofed, building savvy.

Industry/Entity Type

Construction

Requirements
Must have
• We're looking for some wow factor as well and something that stands out and people will remember

The final design should communicate timeless craftsmanship, trust, special, VALUE, exquisite, stylish, standing the test of time, no cutting corners, reliability and high standards.

The final design also needs to be sharp and look great on print. The file supplied needs to be high resolution.

```html
<!DOCTYPE html>
<html lang="en">
<head>
<meta charset="utf-8">
<title>Harbourlight Homes Ltd — Business Card</title>
<link rel="stylesheet" href="https://fonts.googleapis.com/css2?family=Saira:wght@500&family=Questrial&family=Open+Sans:wght@400;700&display=swap">
<style>
  :root {
    --backdrop: #3b3b3c;
    --card-white: #f7f7f6;
    --card-black: #141414;
    --ink: #1c1c1c;
    --brand-red: #d4181f;
    --band-grey: #c9c9c9;
    --badge-navy: #143a78;
    --on-dark: #ededed;
  }
  * { margin: 0; padding: 0; box-sizing: border-box; }
  html, body { width: 1200px; height: 1000px; overflow: hidden; }
  body { background: var(--backdrop); position: relative; font-family: "Questrial", sans-serif; }

  .card {
    position: absolute;
    width: 530px;
    height: 300px;
    border-radius: 14px;
    overflow: hidden;
  }
  .card--front { left: 180px; top: 170px; background: var(--card-white); }
  .card--back  { left: 473px; top: 551px; height: 304px; background: var(--card-black); }

  .brand { position: absolute; height: 60px; }
  .brand__mark { position: absolute; left: 0; top: 2px; width: 56px; height: 56px; background: var(--brand-red); }
  .brand__name {
    position: absolute; left: 71px; top: 3px;
    font-family: "Saira", sans-serif; font-weight: 500;
    font-size: 22px; line-height: 26px; letter-spacing: 1.2px;
    text-transform: uppercase; white-space: nowrap;
  }

  .card--front .brand { left: 36px; top: 50px; width: 270px; }
  .card--front .brand__name { color: var(--ink); }

  .card--back .brand { left: 132px; top: 106px; width: 270px; }
  .card--back .brand__name { color: var(--on-dark); }

  .trade-badge {
    position: absolute; left: 432px; top: 52px;
    width: 60px; height: 66px; background: var(--badge-navy);
  }

  .contact { position: absolute; left: 35px; top: 217px; font-size: 12px; line-height: 15.5px; color: var(--ink); }
  .contact__label { color: var(--brand-red); font-family: "Open Sans", sans-serif; font-weight: 700; }

  .person { position: absolute; right: 44px; top: 214px; text-align: right; color: var(--ink); font-family: "Open Sans", sans-serif; }
  .person__name { font-weight: 700; font-size: 15px; letter-spacing: 0.4px; text-transform: uppercase; }
  .person__role { font-size: 12px; margin-top: 1px; }

  .card__bands { position: absolute; left: 0; bottom: 0; width: 530px; height: 22px; }
</style>
</head>
<body>

  <section class="card card--front" aria-label="Business card front">
    <div class="brand">
      <span class="brand__mark"></span>
      <p class="brand__name">Harbourlight<br>Homes Ltd</p>
    </div>

    <div class="trade-badge" role="img" aria-label="Trusted Trades Federation member badge"></div>

    <div class="contact">
      <p><span class="contact__label">M:</span> 021 555 0148</p>
      <p><span class="contact__label">E:</span> milo@harbourlighthomes.example</p>
      <p><span class="contact__label">W:</span> www.harbourlighthomes.example</p>
    </div>

    <div class="person">
      <p class="person__name">Tobin Vareck</p>
      <p class="person__role">Director</p>
    </div>

    <svg class="card__bands" viewBox="0 0 530 22" aria-hidden="true">
      <polygon points="0,9 325,9 316,22 0,22" fill="var(--band-grey)"/>
      <polygon points="332,0 530,0 530,22 314,22" fill="var(--brand-red)"/>
    </svg>
  </section>

  <section class="card card--back" aria-label="Business card back">
    <div class="brand">
      <span class="brand__mark"></span>
      <p class="brand__name">Harbourlight<br>Homes Ltd</p>
    </div>
  </section>

</body>
</html>
```